New Company Business Card Design

I have a new company logo and I want a new business card design. I dont know if the logo file i attached is in the correct format or quality. We are a New York City Specialty construction Firm specializing in high risk out of the box projects. I want a simple and classy business card that people will his card is as crisp as the work his company does.

Target Market(s)

Clients in the heavy construction industry in New York City

Industry/Entity Type

Construction Company

Contact Information for Business Card

Simple Classy - DIFFERENT

Font styles to use
Other font styles liked:
• Mach the logo font in some way

Colors

Designer to choose colors to be used in the design.

Requirements
Must have
• Uniqueness
Nice to have
• Nothing particular - Just different and classy - Timeless
Should not have
• Goofy Shit or Gimmicky shit

```html
<!DOCTYPE html>
<html lang="en">
<head>
<meta charset="UTF-8">
<title>Ardent Works, Inc. — Business Card</title>
<link rel="stylesheet" href="https://fonts.googleapis.com/css2?family=Arimo:wght@400;700&display=swap">
<style>
  :root {
    --backdrop: #e6e7e9;
    --card-white: #f9f9f9;
    --card-blue: #027bbf;
    --brand-blue: #0f77bd;
    --name-blue: #1a62a3;
    --ink: #1b1b1b;
    --rule: #222222;
    --white: #ffffff;
  }
  * { margin: 0; padding: 0; box-sizing: border-box; }
  html, body {
    width: 1200px;
    height: 1000px;
    overflow: hidden;
    background: var(--backdrop);
    font-family: "Arimo", Arial, sans-serif;
  }
  .card {
    position: absolute;
    left: 251px;
    width: 712px;
    height: 427px;
    box-shadow: 0 3px 8px rgba(0,0,0,0.18);
  }
  .card-front { top: 41px; background: var(--card-white); }
  .card-back { top: 534px; background: var(--card-blue); }

  .holder-name {
    position: absolute;
    right: 50px;
    top: 34px;
    font-size: 22px;
    font-weight: 700;
    color: var(--name-blue);
    letter-spacing: 0.3px;
    white-space: nowrap;
  }

  .wordmark {
    position: absolute;
    font-weight: 700;
    text-align: center;
    line-height: 1;
    white-space: nowrap;
  }
  .wordmark-main { display: block; font-size: 40px; letter-spacing: 0.5px; }
  .wordmark-sub { display: block; font-size: 12px; letter-spacing: 3.5px; margin-top: 9px; }
  .card-front .wordmark { left: 156px; top: 192px; width: 196px; color: var(--brand-blue); }
  .card-back .wordmark { left: 256px; top: 170px; width: 204px; color: var(--white); }
  .card-back .wordmark-main { font-size: 42px; }

  .divider {
    position: absolute;
    left: 372px;
    top: 142px;
    width: 2px;
    height: 173px;
    background: var(--rule);
  }

  .contact-list {
    position: absolute;
    left: 390px;
    top: 148px;
    list-style: none;
  }
  .contact-item {
    display: flex;
    align-items: flex-start;
    font-size: 14px;
    line-height: 16px;
    color: var(--ink);
    white-space: nowrap;
  }
  .contact-icon {
    width: 20px;
    height: 20px;
    margin-right: 17px;
    flex-shrink: 0;
    fill: var(--brand-blue);
  }
  .item-address { height: 46px; }
  .item-phone { height: 37px; }
  .item-mobile { height: 34px; }
  .item-email { height: 31px; }
</style>
</head>
<body>

<section class="card card-front" aria-label="Card front">
  <div class="holder-name">Marcus T. Bellamy</div>

  <div class="wordmark">
    <span class="wordmark-main">ARDENT</span>
    <span class="wordmark-sub">WORKS, INC.</span>
  </div>

  <div class="divider"></div>

  <ul class="contact-list">
    <li class="contact-item item-address">
      <svg class="contact-icon" viewBox="0 0 20 20"><path d="M10 0C6.1 0 3.5 2.8 3.5 6.4 3.5 11 10 20 10 20s6.5-9 6.5-13.6C16.5 2.8 13.9 0 10 0zm0 9a2.6 2.6 0 1 1 0-5.2A2.6 2.6 0 0 1 10 9z"/></svg>
      <span>214 North Pier Road - Linden,<br>New Jersey 07036</span>
    </li>
    <li class="contact-item item-phone">
      <svg class="contact-icon" viewBox="0 0 20 20"><path d="M5.2 1.5l2.4 3.6c.3.5.2 1.1-.2 1.5L6 7.8c.9 2.4 3 4.6 5.6 5.8l1.2-1.3c.4-.4 1-.5 1.5-.2l3.5 2.3c.5.3.6 1 .3 1.5l-1.3 2c-.5.7-1.4 1-2.2.8C8.2 17.3 3 12.1 1.5 5.700c-.2-.8.1-1.7.8-2.2l1.5-1.2c.5-.4 1.1-.3 1.4.2z"/></svg>
      <span>908-555-0142</span>
    </li>
    <li class="contact-item item-mobile">
      <svg class="contact-icon" viewBox="0 0 20 20"><path d="M5.5 0h9c.8 0 1.5.7 1.5 1.5v17c0 .8-.7 1.5-1.5 1.5h-9C4.7 20 4 19.3 4 18.5v-17C4 .7 4.7 0 5.5 0zM6 2.5v8h8v-8H6zm.5 10v1.5h1.5v-1.5H6.5zm3 0v1.5h1.5v-1.5H9.5zm3 0v1.5H14v-1.5h-1.5zm-6 3V17h1.5v-1.5H6.5zm3 0V17h1.5v-1.5H9.5zm3 0V17H14v-1.5h-1.5z"/></svg>
      <span>917-555-0187</span>
    </li>
    <li class="contact-item item-email">
      <svg class="contact-icon" viewBox="0 0 20 20"><path d="M1 4h18v.6L10 11 1 4.6V4zm0 2.6l5.6 4L1 15.4V6.6zm18 0v8.8l-5.6-4.8 5.6-4zM7.9 11.6L10 13.1l2.1-1.5L19 16H1l6.9-4.4z"/></svg>
      <span>marcus@ardentworks.com</span>
    </li>
    <li class="contact-item item-web">
      <svg class="contact-icon" viewBox="0 0 20 20"><path d="M10 1a9 9 0 1 0 0 18 9 9 0 0 0 0-18zm6.9 8h-3c-.1-2.4-.6-4.5-1.4-5.9A7.1 7.1 0 0 1 16.9 9zM10 2.9c.9 1 1.8 3.2 1.9 6.1H8.1C8.2 6.1 9.1 3.9 10 2.9zM7.5 3.1C6.7 4.5 6.2 6.6 6.1 9h-3a7.1 7.1 0 0 1 4.4-5.9zM3.1 11h3c.1 2.4.6 4.5 1.4 5.9A7.1 7.1 0 0 1 3.1 11zm6.9 6.1c-.9-1-1.8-3.2-1.9-6.1h3.8c-.1 2.9-1 5.1-1.9 6.1zm2.5-.2c.8-1.4 1.3-3.5 1.4-5.9h3a7.1 7.1 0 0 1-4.4 5.9z"/></svg>
      <span>www.ardentworks.com</span>
    </li>
  </ul>
</section>

<section class="card card-back" aria-label="Card back">
  <div class="wordmark">
    <span class="wordmark-main">ARDENT</span>
    <span class="wordmark-sub">WORKS, INC.</span>
  </div>
</section>

</body>
</html>
```